Flyer
Zielgruppe
Wir sind ein ambulanter Pflegedienst, Wir versorgen hilfebedürftige Menschen. Haben sie schon Erfahrung mit ambulanten Pflegediensten?
Aufgabenstellung
Er sollte kurz und knapp sein, nicht zu viel Text.

```html
<!DOCTYPE html>
<html lang="de">
<head>
<meta charset="utf-8">
<title>Flyer – Ambulante Pflege Berger &amp; Harms</title>
<link rel="stylesheet" href="https://fonts.googleapis.com/css2?family=Montserrat:wght@400;500;600;700&display=swap">
<style>
  :root{
    --sage:#7c9b6c;
    --sage-dark:#2f6a3a;
    --title-green:#6c8a57;
    --paper:#e5e9df;
    --beige:#b7b69b;
    --olive:#7b8a55;
    --teal:#5db1a6;
    --red:#e0231c;
    --ink:#3a3f36;
    --muted:#8e918a;
    --white:#ffffff;
    --stage:#ffffff;
  }
  *{box-sizing:border-box;margin:0;padding:0}
  html,body{width:1200px;height:848px;overflow:hidden;background:var(--stage);font-family:"Montserrat",sans-serif}
  .canvas{position:relative;width:1200px;height:848px}
  .page{position:absolute;top:44px;width:538px;height:760px}

  /* Front page */
  .front{left:42px;background:var(--sage);color:var(--white)}
  .brand{position:absolute;top:130px;left:0;right:0;display:flex;align-items:center;justify-content:center;gap:12px}
  .brand-dot{width:22px;height:22px;border-radius:50%;background:var(--red)}
  .brand-name{font-size:21px;font-weight:600;color:var(--white);letter-spacing:.3px}
  .hero-band{position:absolute;top:233px;left:0;width:100%;height:250px;background:var(--sage-dark)}
  .hero-photo{position:absolute;top:0;left:108px;width:340px;height:250px;
    clip-path:polygon(14% 0,100% 0,86% 100%,0 100%);
    background:linear-gradient(150deg,#7d8b55 0%,#c98a52 35%,#d7b08a 55%,#b4603c 75%,#5f7a45 100%)}
  .hero-banner{position:absolute;left:210px;top:428px;width:328px;height:58px;background:var(--red);
    clip-path:polygon(4% 0,100% 0,100% 100%,0 100%);
    display:flex;flex-direction:column;justify-content:center;padding-left:28px;
    font-size:17px;font-weight:600;line-height:1.15;letter-spacing:.3px}
  .contact{position:absolute;top:545px;left:42px;right:30px;font-size:11px;line-height:1.75}
  .contact-row{display:flex;gap:30px}
  .contact-col{flex:1;display:flex;gap:8px}
  .contact-col svg{flex:none;margin-top:4px}
  .contact-line{display:flex;gap:8px;align-items:center}
  .contact-line svg{margin-top:0}
  .contact-indent{padding-left:20px}
  .contact-rule{height:1px;background:rgba(255,255,255,.55);margin:14px 0}

  /* Services page */
  .services{left:620px;background:var(--paper);color:var(--ink)}
  .services-title{position:absolute;top:148px;left:22px;font-size:40px;font-weight:600;color:var(--title-green);letter-spacing:1px}
  .services-grid{position:absolute;left:0;width:100%;display:flex}
  .services-grid.top{top:210px}
  .services-grid.bottom{top:525px}
  .service-col{flex:1}
  .service-head{height:42px;display:flex;align-items:center;padding:0 14px;font-size:10.5px;font-weight:600;line-height:1.3;color:var(--ink)}
  .head-beige{background:var(--beige)}
  .head-sage{background:var(--sage)}
  .head-olive{background:var(--olive)}
  .head-teal{background:var(--teal)}
  .service-list{list-style:none;padding:14px 10px 0 26px;font-size:10.5px;line-height:1.56}
  .service-list li{position:relative}
  .service-list li::before{content:"";position:absolute;left:-11px;top:7px;width:4px;height:4px;border-radius:50%;background:var(--ink)}
  .service-list .note{color:var(--muted)}
  .service-list .note::before{display:none}
  .price-note{position:absolute;left:332px;top:690px;width:160px;display:flex;align-items:center;gap:10px;font-size:9.5px;line-height:1.4;text-align:left}
  .price-dot{flex:none;width:38px;height:38px;border-radius:50%;background:var(--sage)}
</style>
</head>
<body>
<div class="canvas">

  <section class="page front">
    <div class="brand">
      <span class="brand-dot"></span>
      <span class="brand-name">Ambulante Pflege Berger &amp; Harms</span>
    </div>

    <div class="hero-band">
      <div class="hero-photo" role="img" aria-label="Luftaufnahme der Ortschaft mit Dächern und Grünflächen"></div>
    </div>
    <div class="hero-banner">
      <span>VERSORGUNG 30 KM RUND</span>
      <span>UM AUENTAL</span>
    </div>

    <div class="contact">
      <div class="contact-row">
        <div class="contact-col">
          <svg width="10" height="13" viewBox="0 0 10 13"><path d="M5 0a5 5 0 0 1 5 5c0 3.5-5 8-5 8S0 8.5 0 5a5 5 0 0 1 5-5z" fill="#fff"/><circle cx="5" cy="5" r="1.8" fill="#7c9b6c"/></svg>
          <div>Ambulante Pflege Berger &amp; Harms<br>Lindenweg 12<br>84490 Auental</div>
        </div>
        <div class="contact-col">
          <div>
            <div class="contact-line"><svg width="12" height="9" viewBox="0 0 12 9"><rect width="12" height="9" fill="#fff"/><path d="M0 0l6 5 6-5" stroke="#7c9b6c" fill="none"/></svg>E-Mail: info@pflege-auental.de</div>
            <div class="contact-line"><svg width="12" height="12" viewBox="0 0 12 12"><circle cx="6" cy="6" r="5.5" fill="#fff"/><circle cx="6" cy="6" r="2.2" fill="#7c9b6c"/></svg>Bürozeiten:</div>
            <div class="contact-indent">Mo-Fr 08:00-16:00</div>
          </div>
        </div>
      </div>
      <div class="contact-rule"></div>
      <div class="contact-row">
        <div class="contact-col"><div>Frau Lena Berger, Inhaberin<br>
          <span class="contact-line"><svg width="11" height="11" viewBox="0 0 11 11"><path d="M2 0l2 3-1 1.5a7 7 0 0 0 3.5 3.5L8 7l3 2-1.5 2C4 11 0 7 0 1.5z" fill="#fff"/></svg>01701234567</span></div></div>
        <div class="contact-col"><div>Herr Jonas Harms, Inhaber<br>
          <span class="contact-line"><svg width="11" height="11" viewBox="0 0 11 11"><path d="M2 0l2 3-1 1.5a7 7 0 0 0 3.5 3.5L8 7l3 2-1.5 2C4 11 0 7 0 1.5z" fill="#fff"/></svg>015200012345</span></div></div>
      </div>
    </div>
  </section>

  <section class="page services">
    <h1 class="services-title">UNSERE LEISTUNGEN</h1>

    <div class="services-grid top">
      <div class="service-col">
        <div class="service-head head-beige">GRUNDPFLEGE NACH SGB XI</div>
        <ul class="service-list">
          <li>Körperpflege, Duschen,</li>
          <li>Waschen, Baden, Hautpflege,</li>
          <li>Hilfe beim An- und Auskleiden</li>
          <li class="note">(Mundpflege, Rasieren, Kämmen, Haar- und Nagelpflege, Hilfe bei der Nahrungsaufnahme)</li>
          <li>Verabreichung von Sondennahrung</li>
          <li>Stoma Pflege</li>
          <li>Inkontinenzversorgung</li>
          <li>Lagern</li>
          <li>Mobilisieren</li>
        </ul>
      </div>
      <div class="service-col">
        <div class="service-head head-sage">BEHANDLUNGSPFLEGE NACH SGB V /<br>NACH ÄRZTLICHER ANORDNUNG</div>
        <ul class="service-list">
          <li>Moderne Wundversorgung</li>
          <li>akute und chronische Wunden</li>
          <li>Dekubitus Behandlung</li>
          <li>Injektionen und Infusionen</li>
          <li>Blutzucker Messung</li>
          <li>Blutdruck und Puls Messung</li>
          <li>PEG und PuFi-Versorgung</li>
          <li>Schmerztherapie mit Schmerzpumpe</li>
          <li>Medikamentenbox richten</li>
          <li>Medikamente verabreichen</li>
          <li>Kompressionstherapie</li>
          <li>Stomaversorgung</li>
        </ul>
      </div>
    </div>

    <div class="services-grid bottom">
      <div class="service-col">
        <div class="service-head head-olive">ZUSATZLEISTUNGEN</div>
        <ul class="service-list">
          <li>Hauswirtschaftliche Versorgung</li>
          <li>Hausnotruf durch Kooperationspartner</li>
          <li>Verhinderungspflege und</li>
          <li>Entlastung der Angehörigen</li>
          <li>Essen auf Rädern</li>
          <li>24 Stunden Rufbereitschaft</li>
          <li>Beratungseinsätze nach § 37 Abs. 3 SGB XI</li>
          <li class="note">(Bei Bezug von Pflegegeld)</li>
        </ul>
      </div>
      <div class="service-col">
        <div class="service-head head-teal">ENTLASTUNGSLEISTUNGEN</div>
        <ul class="service-list">
          <li>Spaziergänge</li>
          <li>Beschäftigung</li>
          <li>Hauswirtschaftliche Leistungen</li>
          <li>Betreuungsmaßnahmen</li>
        </ul>
      </div>
    </div>

    <div class="price-note">
      <span class="price-dot"></span>
      <span>Die Leistung beträgt pauschal 131 € im Monat für Pflegegrad 1-5</span>
    </div>
  </section>

</div>
</body>
</html>
```